Sickle Cell Patient Flyer

I need this be appealing to families dealing with sickle cell disease. Both informative-introducing the idea that a stroke prevention program is not only easy for their children but necessary. Stroke is a risk to all with children with SCD.
I included a few info flyers from the Brainward Alliance and licensed to me photos I like. I am open to suggestions.
web address is carebrightpath.example
Call to schedule 855-555-0148
TCD is a safe and accurate tool that makes stroke prevention possible for your SCD patients and family.
Risk is highest for SCD sufferers age 2 to 5. Protect your childs future.

Target Market(s)

Parents, families and medical professionals

Industry/Entity Type

Medical wellness

Font styles to use
Other font styles liked:
• something close to my logo font

Colors
0094D4
00A9DD
6FCCEA
C7EBF8
E9F6FB

Requirements
Nice to have
• pictures of kids (Children of color) pictures of Brains, kids happy with medical professionals
Should not have
• dark colors

```html
<!DOCTYPE html>
<html lang="en">
<head>
<meta charset="utf-8">
<title>Sickle Cell Stroke Prevention Flyer</title>
<link href="https://fonts.googleapis.com/css2?family=Open+Sans:wght@400;600;700&family=Source+Sans+3:wght@400;600;700&family=Kaushan+Script&display=swap" rel="stylesheet">
<style>
  :root {
    --backdrop: #3a3839;
    --sky: #a9d5f2;
    --navy: #0b3470;
    --navy-deep: #062a5e;
    --green: #3f9370;
    --mint: #6fc4a0;
    --ocean: #1c7fc4;
    --ink: #1b2433;
    --white: #ffffff;
  }
  * { margin: 0; padding: 0; box-sizing: border-box; }
  html, body { width: 1200px; height: 1200px; overflow: hidden; background: var(--backdrop); }
  .flyer {
    position: absolute; left: 136px; top: 0;
    width: 1332px; height: 1723px;
    transform: scale(0.69646); transform-origin: top left;
    background: var(--sky); overflow: hidden;
    font-family: "Source Sans 3", sans-serif; color: var(--ink);
  }
  .shapes { position: absolute; inset: 0; }
  .hero-title {
    position: absolute; left: 50px; top: 52px; width: 640px;
    font-family: "Open Sans", sans-serif;
    color: var(--white); font-size: 43px; line-height: 61px; font-weight: 400; letter-spacing: -0.3px;
  }
  .brand {
    position: absolute; left: 790px; top: 150px; width: 470px;
    display: flex; align-items: center; justify-content: center; gap: 18px;
  }
  .brand-mark { width: 50px; height: 50px; background: var(--ocean); }
  .brand-name { font-family: "Open Sans", sans-serif; font-size: 54px; font-weight: 700; color: var(--navy); }
  .risk-block { position: absolute; left: 715px; top: 462px; width: 572px; text-align: center; }
  .risk-title {
    font-weight: 700; color: var(--navy);
    font-size: 39px; line-height: 43px; letter-spacing: -0.3px;
  }
  .risk-sub {
    margin-top: 8px; font-weight: 600;
    font-size: 29px; line-height: 32px; color: var(--ink); letter-spacing: -0.3px;
  }
  .risk-rule { width: 245px; height: 3px; background: var(--ink); margin: 15px auto 14px; }
  .risk-body { text-align: justify; font-size: 26.5px; line-height: 36px; letter-spacing: -0.3px; }
  .services {
    position: absolute; left: 75px; top: 905px; width: 1177px; height: 143px;
    background: var(--green); border: 3px solid var(--white); border-radius: 12px;
    box-shadow: 0 18px 18px -10px rgba(6,42,94,.35);
    display: flex; align-items: center; padding-left: 30px;
  }
  .service { display: flex; align-items: center; gap: 18px; margin-right: 38px; }
  .service-icon { width: 92px; height: 92px; }
  .service-name { font-family: "Kaushan Script", cursive; color: var(--white); font-size: 52px; }
  .facts { position: absolute; left: 45px; top: 1100px; width: 522px; list-style: none; }
  .facts li {
    position: relative; padding-left: 38px; font-size: 27px; line-height: 35px;
    margin-bottom: 34px; text-align: justify;
  }
  .facts li b { font-weight: 700; }
  .facts svg { position: absolute; left: 0; top: 6px; width: 26px; height: 26px; }
  .contact-bar {
    position: absolute; left: 0; top: 1575px; width: 1332px; height: 148px;
    background: var(--navy-deep); border-top: 7px solid var(--mint); color: var(--white);
    font-family: "Open Sans", sans-serif;
  }
  .call-label { position: absolute; left: 55px; top: 8px; font-family: "Kaushan Script", cursive; font-size: 40px; }
  .call-number {
    position: absolute; left: 52px; top: 58px; display: flex; align-items: center; gap: 6px;
    font-size: 62px; font-weight: 700; letter-spacing: -1px;
  }
  .divider { position: absolute; top: 28px; height: 100px; border-left: 2px dotted rgba(255,255,255,.7); }
  .contact-lines { position: absolute; left: 577px; top: 28px; font-size: 33px; font-weight: 600; line-height: 52px; }
  .contact-lines div { display: flex; align-items: center; gap: 14px; }
  .social { position: absolute; left: 1140px; top: 58px; display: flex; gap: 12px; }
  .social span { width: 38px; height: 38px; border-radius: 50%; background: var(--mint); }
</style>
</head>
<body>
<main class="flyer">
  <svg class="shapes" viewBox="0 0 1332 1723" width="1332" height="1723">
    <defs>
      <linearGradient id="heroFill" x1="0" y1="0" x2="0.6" y2="1">
        <stop offset="0" stop-color="#5c5c58"/><stop offset="1" stop-color="#3c3d3f"/>
      </linearGradient>
      <radialGradient id="heroWarm" cx="0.5" cy="0.5" r="0.5">
        <stop offset="0" stop-color="#f0b428" stop-opacity="0.85"/><stop offset="0.55" stop-color="#e0a526" stop-opacity="0.45"/><stop offset="1" stop-color="#e0a526" stop-opacity="0"/>
      </radialGradient>
      <linearGradient id="ringFill" x1="0" y1="0" x2="0" y2="1">
        <stop offset="0" stop-color="#6fc4a0"/><stop offset="1" stop-color="#3f8fd6"/>
      </linearGradient>
      <radialGradient id="orbFill" cx="0.5" cy="0.5" r="0.55">
        <stop offset="0" stop-color="#1a9bc0"/><stop offset="0.6" stop-color="#1a5aa8"/><stop offset="1" stop-color="#233a8c"/>
      </radialGradient>
      <radialGradient id="orbGlow" cx="0.5" cy="0.5" r="0.5">
        <stop offset="0" stop-color="#0d1a2c"/><stop offset="0.6" stop-color="#0f2f55" stop-opacity="0.7"/><stop offset="1" stop-color="#0f2f55" stop-opacity="0"/>
      </radialGradient>
      <radialGradient id="orbSpark" cx="0.5" cy="0.5" r="0.5">
        <stop offset="0" stop-color="#5fe6ea" stop-opacity="0.55"/><stop offset="1" stop-color="#5fe6ea" stop-opacity="0"/>
      </radialGradient>
      <clipPath id="heroClip"><path d="M640 0 C735 160 740 510 460 742 C320 840 130 842 0 822 V0 Z"/></clipPath>
    </defs>
    <path d="M660 0 H1332 V300 C1200 380 1080 405 960 400 C860 395 790 370 735 345 L735 0 Z" fill="#ffffff"/>
    <path d="M735 345 C850 395 960 410 1060 398 C1160 386 1250 345 1332 300" fill="none" stroke="#0b3470" stroke-width="14"/>
    <path d="M660 0 C760 160 770 520 480 760 C330 860 130 860 0 835 V0 Z" fill="url(#ringFill)"/>
    <g role="img" aria-label="Photo of a smiling child in a yellow sweater raising both arms in front of chalk-drawn brain outlines">
      <path d="M640 0 C735 160 740 510 460 742 C320 840 130 842 0 822 V0 Z" fill="url(#heroFill)"/>
      <g clip-path="url(#heroClip)">
        <ellipse cx="330" cy="700" rx="240" ry="300" fill="url(#heroWarm)"/>
      </g>
    </g>
    <g role="img" aria-label="Illustration of a child's head silhouette in profile with a glowing network of brain connections">
      <circle cx="1100" cy="1450" r="510" fill="url(#orbFill)"/>
      <ellipse cx="1010" cy="1310" rx="300" ry="330" fill="url(#orbGlow)"/>
      <ellipse cx="1000" cy="1240" rx="230" ry="200" fill="url(#orbSpark)"/>
    </g>
  </svg>

  <h1 class="hero-title">Stroke Prevention for<br>Children with children with<br>sickle cell disease is possible!</h1>

  <div class="brand"><span class="brand-mark"></span><span class="brand-name">CareBright Path</span></div>

  <section class="risk-block">
    <h2 class="risk-title">SICKLE CELL DISEASE RAISES<br>A CHILD’S STROKE RISK.</h2>
    <p class="risk-sub">CLOSE EVALUATION AND TREATMENT<br>MAY HELP PREVENT STROKE.</p>
    <div class="risk-rule"></div>
    <p class="risk-body">Health screening from CareBright Path can help detect issues, when they’re easier to treat. CareBright Path is staffed by technologists and physicians with years of clinical experience in the nation’s leading medical centers. We understand disease and how to diagnose it.</p>
  </section>

  <section class="services">
    <div class="service">
      <svg class="service-icon" viewBox="0 0 92 92">
        <circle cx="46" cy="46" r="43" fill="#3a9cc4" stroke="#0b3470" stroke-width="3"/>
        <path d="M34 22 v16 a10 10 0 0 0 20 0 V22 M44 48 v10 a12 12 0 0 0 24 0 v-6" fill="none" stroke="#fff" stroke-width="3"/>
        <circle cx="68" cy="49" r="5" fill="none" stroke="#fff" stroke-width="3"/>
      </svg>
      <span class="service-name">Preventive Screening</span>
    </div>
    <div class="service">
      <svg class="service-icon" viewBox="0 0 92 92">
        <circle cx="46" cy="46" r="43" fill="#3a9cc4" stroke="#0b3470" stroke-width="3"/>
        <path d="M46 70 L22 46 a13 13 0 0 1 24 -16 a13 13 0 0 1 24 16 Z" fill="none" stroke="#fff" stroke-width="3"/>
        <path d="M18 46 h16 l5 -9 l6 16 l5 -10 h24" fill="none" stroke="#fff" stroke-width="3"/>
      </svg>
      <span class="service-name">Corporate Wellness</span>
    </div>
  </section>

  <ul class="facts">
    <li><svg viewBox="0 0 26 26"><circle cx="13" cy="13" r="11" fill="none" stroke="#0b3470" stroke-width="2"/><path d="M8 13 l4 4 l7 -8" fill="none" stroke="#0b3470" stroke-width="2"/></svg>Simple and <b>painless screening</b> for your child.</li>
    <li><svg viewBox="0 0 26 26"><circle cx="13" cy="13" r="11" fill="none" stroke="#0b3470" stroke-width="2"/><path d="M8 13 l4 4 l7 -8" fill="none" stroke="#0b3470" stroke-width="2"/></svg>Our Screening uses <b>ultrasound</b> which is transcranial doppler.</li>
    <li><svg viewBox="0 0 26 26"><circle cx="13" cy="13" r="11" fill="none" stroke="#0b3470" stroke-width="2"/><path d="M8 13 l4 4 l7 -8" fill="none" stroke="#0b3470" stroke-width="2"/></svg>About <b>11% of SCD patients</b> have strokes before <b>age 20</b> with the highest risk between <b>age 2 and 5</b>.</li>
    <li><svg viewBox="0 0 26 26"><circle cx="13" cy="13" r="11" fill="none" stroke="#0b3470" stroke-width="2"/><path d="M8 13 l4 4 l7 -8" fill="none" stroke="#0b3470" stroke-width="2"/></svg>Screening or early signs of stroke can be a tool to for early diagnosis allowing for treatments that eliminate the risk.</li>
  </ul>

  <footer class="contact-bar">
    <div class="call-label">Call to Schedule</div>
    <div class="call-number">
      <svg width="38" height="44" viewBox="0 0 24 24"><path d="M6.6 10.8a15 15 0 0 0 6.6 6.6l2.2-2.2a1 1 0 0 1 1-.25 11.4 11.4 0 0 0 3.6.57 1 1 0 0 1 1 1V20a1 1 0 0 1-1 1A17 17 0 0 1 3 4a1 1 0 0 1 1-1h3.5a1 1 0 0 1 1 1 11.4 11.4 0 0 0 .57 3.6 1 1 0 0 1-.25 1z" fill="#6fc4e6"/></svg>
      855-555-0148
    </div>
    <div class="divider" style="left:555px"></div>
    <div class="contact-lines">
      <div><svg width="30" height="26" viewBox="0 0 30 26"><rect x="2" y="6" width="26" height="18" fill="none" stroke="#6fc4a0" stroke-width="2.5"/><path d="M2 6 l13 10 l13 -10" fill="none" stroke="#6fc4a0" stroke-width="2.5"/></svg>info@carebrightpath.example</div>
      <div><svg width="30" height="30" viewBox="0 0 30 30"><circle cx="15" cy="15" r="12" fill="none" stroke="#6fc4a0" stroke-width="2.5"/><path d="M3 15 h24 M15 3 c-7 8 -7 16 0 24 c7 -8 7 -16 0 -24" fill="none" stroke="#6fc4a0" stroke-width="2"/></svg>www.carebrightpath.example/</div>
    </div>
    <div class="divider" style="left:1113px"></div>
    <div class="social"><span></span><span></span><span></span></div>
  </footer>
</main>
</body>
</html>
```